Stage Design Company Business Card

We are looking to step up up our business card design for our team.

We are a Full service Design and Consultation company for Stage and TV with an emphasis in Theatrical Lighting.

We like our materials to be clean and modern with solid colors free of patterns and gradients. Our brand consists of 4 primary colors Purple, Black, Grey, and White. Provided is our Word Mark as well as our Symbol Logo.

We would like our cards to leave an impression beyond the information, show our attention to design and detail, and make our marks an easily recognized feature (together or apart) for our clients.

We need a warm approachable comfortable feel for some clients, and a professional flair for the board member type clients.

Attached are our brand elements, and our existing cards to give a sense of our style and a glipse at the information we provide on our cards.

Target Market(s)

broad client base from church leaders to high school teachers and architects.

Industry/Entity Type

Business

Contact Information for Business Card

We format our phone number with periods not parenthesis or dashes. Information will be edited for each of our team members, and team member specific cards are not part of this scope, but rather a template so to speak.

Font styles to use
Sans Serif

Colors
6b449b
ffffff
000000
333333
aaaaaa

Requirements
Must have
• Wordmark and logo mark present (does not need to exist on the same side of card)
• Brand Colors,
• Name, Phone, Email, Address.
• Unique choices that make someone stop and take a second look
Nice to have
• It would be nice to somehow convey what we DO, as our brand name does not lend itself to this, outside of an obvious tagline though.....
• social media if not crowded. all of our handles match (instagram, twitter, facebook)
Should not have
• "clipart"

```html
<!DOCTYPE html>
<html lang="en">
<head>
<meta charset="utf-8">
<title>Halvern Business Card</title>
<link rel="stylesheet" href="https://fonts.googleapis.com/css2?family=Source+Sans+3:ital,wght@0,400;0,600;0,700;1,600&display=swap">
<style>
  :root {
    --backdrop: #5f5f5f;
    --card-light: #ffffff;
    --card-dark: #121821;
    --ink: #111318;
    --ink-soft: #2b2d33;
    --rule: #3a3c42;
    --mark-light: #c9cbd0;
    --tagline: #b4b7bf;
  }
  * { margin: 0; padding: 0; box-sizing: border-box; }
  html, body { width: 1200px; height: 900px; overflow: hidden; }
  body {
    background: var(--backdrop);
    font-family: "Source Sans 3", "Helvetica Neue", Arial, sans-serif;
    position: relative;
  }
  .card { position: absolute; top: 306px; width: 440px; height: 272px; }
  .card--front { left: 149px; background: var(--card-light); color: var(--ink); }
  .card--back { left: 608px; background: var(--card-dark); }

  .brand { position: absolute; display: flex; flex-direction: column; align-items: center; }
  .brand--front { left: 62px; top: 88px; width: 140px; }
  .brand__dot { width: 44px; height: 44px; border-radius: 50%; background: var(--ink); margin-bottom: 44px; }
  .brand__name {
    font-size: 20px; font-weight: 600; letter-spacing: 9px; line-height: 1;
    margin-right: -9px;
  }
  .brand--front .brand__name { color: var(--ink); }

  .divider { position: absolute; left: 224px; top: 74px; width: 1px; height: 123px; background: var(--rule); }

  .contact { position: absolute; left: 249px; top: 70px; color: var(--ink-soft); }
  .contact__name { font-size: 15px; font-weight: 600; color: var(--ink); line-height: 18px; letter-spacing: 0.2px; }
  .contact__role { font-size: 12.5px; line-height: 15px; margin-bottom: 9px; }
  .contact__list { list-style: none; }
  .contact__item { display: flex; align-items: center; font-size: 12.5px; line-height: 16px; }
  .contact__item svg { width: 9px; height: 9px; margin-right: 6px; fill: var(--ink); }
  .contact__address { font-size: 12.5px; line-height: 16px; margin-top: 7px; }

  .brand--back { left: 62px; top: 95px; flex-direction: row; align-items: center; }
  .brand--back .brand__dot { background: var(--mark-light); width: 64px; height: 64px; margin: 0 46px 0 0; }
  .brand--back .brand__name { color: var(--mark-light); font-size: 30px; letter-spacing: 17px; margin-right: -17px; }

  .tagline {
    position: absolute; left: 0; right: 0; top: 208px;
    text-align: center; color: var(--tagline);
    font-size: 13px; font-weight: 600; font-style: italic; line-height: 17px;
  }
</style>
</head>
<body>
  <section class="card card--front" aria-label="Business card front">
    <div class="brand brand--front">
      <span class="brand__dot"></span>
      <span class="brand__name">HALVERN</span>
    </div>
    <span class="divider"></span>
    <div class="contact">
      <p class="contact__name">MARCUS HALE</p>
      <p class="contact__role">Managing Director</p>
      <ul class="contact__list">
        <li class="contact__item">
          <svg viewBox="0 0 10 10" aria-hidden="true"><path d="M2 0.5 L3.6 2.8 L2.7 3.8 C3.3 5.1 4.9 6.7 6.2 7.3 L7.2 6.4 L9.5 8 L8.6 9.5 C4.5 9.3 0.7 5.5 0.5 1.4 Z"/></svg>
          (044)123456789
        </li>
        <li class="contact__item">
          <svg viewBox="0 0 10 10" aria-hidden="true"><path d="M0.5 2 H9.5 V8.5 H0.5 Z M1.2 2.6 L5 5.4 L8.8 2.6 V3.4 L5 6.2 L1.2 3.4 Z" fill-rule="evenodd"/></svg>
          info@youremail.com
        </li>
        <li class="contact__item">
          <svg viewBox="0 0 10 10" aria-hidden="true"><circle cx="5" cy="5" r="4.5"/></svg>
          www.websitename.com
        </li>
      </ul>
      <p class="contact__address">1234, Address GoesHere,<br>Country name, 12345</p>
    </div>
  </section>

  <section class="card card--back" aria-label="Business card back">
    <div class="brand brand--back">
      <span class="brand__dot"></span>
      <span class="brand__name">HALVERN</span>
    </div>
    <p class="tagline">Design and Consultation company for Stage<br>and TV with an emphasis in Theatrical Lighting.</p>
  </section>
</body>
</html>
```